palduro.org business card design

We need 2-sided business cards for palduro.org; one side will be printed in English (EN), the other in Spanish (ES); the information represnted will be the same.
We are a non-profit that aims to mentor and coach future leaders / visionaries. Our target markets are developing countries (Latin America, Africa, Asia) rather than the developed ("western") world. Our business model works by finding funding to mentor / coach a candidate. We provide several mentors / coaches per candidate which help translate the candidate's vision / dream into a path with objectives and steps.
We want the business cards to transmit our values, which are: innovation, learning / self-improvement, equality (i.e. free from discrimination), boldness, intelligence, thoughtfulness, culture, society, future, sustainability.
We recommend the designers work with these values to produce a bold and innovative design, which does not need to adhere to the traditional criteria for business cards. Please use fresh (modern) colours.

Target Market(s)

Visionaries and thought leaders all over the world, but initially in Latin America. We don't discriminate on age, sex, religion, race or any other difference between people

Industry/Entity Type

Leadership

Contact Information for Business Card

The business cards will contain one language (English / Spanish) per side. It would be nice to have some continuity between the front and the back (e.g. pattern, colours).
Each side will contain the company name, website (www.palduro.org) and a slogan / mantra (which will be provided and can be represented as a placeholder until such time). The other details will be Name, (Function), and contact details (email and phone number).

Font styles to use
Sans Serif

Colors

Designer to choose colors to be used in the design.

Requirements
Must have
• [Side A: ENGLISH --- COMPANY INFO]
• [Company Name] Palduro
• [Slogan / Mantra] Shape your world!
• [Website] palduro.org
• [Side A: ENGLISH --- PERSONAL INFO]
• [Name] Tim Hallox
• [Job Title] Mentoring Coordinator
• [Phone / WhatsApp] +51 917 208 386
• [eMail] tim@palduro.org
• [Side B: SPANISH --- COMPANY INFO]
• [Company Name] Palduro
• [Slogan / Mantra] ¡Moldea tu mundo!
• [Website] palduro.org
• [Side B: SPANISH --- PERSONAL INFO]
• [Name] Timothy Hallox
• [Job Title] Coordinador de Mentoreo
• [eMail] tim@palduro.org
• [SIDE A: ENGLISH --- Central Values]
• - Future
• - Growth
• - Leadership
• [SIDE B: SPANISH --- Central Values]
• - Futuro
• - Liderazgo
• - Crecimiento
Nice to have
• Innovative and different design. Modern and fresh. Bold and clever.
• Secondary Values (we would like represented) are:
• [SIDE A: ENGLISH --- Secondary Values]
• - Equality
• - Innovation
• - Sustainability
• [SIDE B: SPANISH --- Secondary Values]
• - Igualdad
• - Innovación
• - Sostenibilidad
Should not have
• Please note that the images I have attached to this brief are just some images that I liked while browsing for material for the website. It does not imply I want these colours or this type of design, just that I felt these images had a good feel.

```html
<!DOCTYPE html>
<html lang="en">
<head>
<meta charset="utf-8">
<title>Palduro business card – ES and EN sides</title>
<link rel="stylesheet" href="https://fonts.googleapis.com/css2?family=Roboto:wght@400;500;700;900&display=swap">
<style>
  :root {
    --yellow: #fdf000;
    --magenta: #ea0f8c;
    --ink: #111111;
    --white: #ffffff;
    --globe-blue: #2b3c9e;
    --page: #ecebe7;
  }
  * { box-sizing: border-box; margin: 0; padding: 0; }
  html, body { width: 900px; height: 1200px; overflow: hidden; }
  body {
    background: var(--page);
    font-family: "Roboto", Arial, sans-serif;
    position: relative;
  }
  .card {
    position: absolute;
    left: 85px;
    width: 733px;
    height: 428px;
    border-radius: 22px;
    overflow: hidden;
  }
  .card--es { top: 138px; background: var(--yellow); color: var(--ink); }
  .card--en { top: 633px; background: var(--magenta); color: var(--white); }

  .motif {
    position: absolute;
    left: 330px; top: -10px;
    width: 420px; height: 400px;
    border-radius: 40px;
  }
  .card--es .motif { background: radial-gradient(ellipse at center, rgba(245,190,0,.55), rgba(245,190,0,0) 70%); }
  .card--en .motif { background: radial-gradient(ellipse at center, rgba(255,255,255,.22), rgba(255,255,255,0) 70%); }

  .brand { position: absolute; left: 40px; top: 50px; display: flex; align-items: center; }
  .brand__dot { width: 120px; height: 120px; border-radius: 50%; background: var(--globe-blue); flex: none; }
  .brand__text { margin-left: 25px; }
  .brand__name { font-size: 48px; font-weight: 900; line-height: 1; letter-spacing: .5px; }
  .brand__slogan { font-size: 18px; font-weight: 500; margin-top: 4px; }
  .card--es .brand__slogan { color: var(--magenta); }
  .card--en .brand__slogan { color: var(--yellow); }

  .person { position: absolute; left: 38px; top: 242px; }
  .person__name { font-size: 28px; font-weight: 700; line-height: 1.1; }
  .person__role { font-size: 16px; font-weight: 500; margin-top: 6px; letter-spacing: .3px; }
  .card--es .person__role { color: var(--magenta); }
  .card--en .person__role { color: var(--yellow); }

  .rule { position: absolute; left: 38px; top: 313px; width: 655px; height: 1.5px; }
  .card--es .rule { background: var(--ink); }
  .card--en .rule { background: var(--white); }

  .contacts {
    position: absolute; left: 38px; top: 324px; width: 660px;
    display: flex; align-items: center; font-size: 19px; font-weight: 500;
  }
  .contacts__sep { margin: 0 14px; }
  .icon { width: 26px; height: 26px; flex: none; margin-right: 6px; }
  .contacts__item { display: flex; align-items: center; }

  .bands { position: absolute; left: 0; top: 0; width: 733px; height: 428px; }
  .values { position: absolute; white-space: nowrap; }
  .values--core { left: 37px; top: 397px; font-size: 19px; font-weight: 500; color: var(--white); }
  .values--more { left: 402px; top: 402px; font-size: 15px; font-weight: 500; }
  .card--es .values--more { color: var(--white); }
  .card--en .values--more { color: var(--ink); left: 405px; top: 403px; }
  .bullet { display: inline-block; width: 6px; height: 6px; border-radius: 50%; margin: 0 4px 3px; vertical-align: middle; }
  .values--core .bullet { background: var(--white); }
  .card--en .values--core .bullet { background: var(--yellow); }
  .card--es .values--more .bullet { background: var(--white); }
  .card--en .values--more .bullet { background: var(--magenta); }
</style>
</head>
<body>

<section class="card card--es" lang="es">
  <div class="motif" role="img" aria-label="Motivo decorativo tenue del emblema de la organización"></div>

  <div class="brand">
    <div class="brand__dot"></div>
    <div class="brand__text">
      <div class="brand__name">PALDURO</div>
      <div class="brand__slogan">¡MOLDEA TU MUNDO!</div>
    </div>
  </div>

  <div class="person">
    <div class="person__name">TIMOTHY HALLOX</div>
    <div class="person__role">COORDINADOR DE MENTOREO</div>
  </div>

  <div class="rule"></div>

  <div class="contacts">
    <span class="contacts__item">
      <svg class="icon" viewBox="0 0 26 26"><circle cx="13" cy="13" r="13" fill="#ea0f8c"/><path d="M9 7c1 0 2 2 2 3s-1 1-1 2 3 4 4 4 1-1 2-1 3 1 3 2-1 2-3 2C12 19 7 14 7 9c0-1 1-2 2-2z" fill="#fff"/></svg>
      <svg class="icon" viewBox="0 0 26 26"><circle cx="13" cy="13" r="11.5" fill="none" stroke="#ea0f8c" stroke-width="2"/><rect x="7.5" y="8.5" width="11" height="7" rx="2" fill="#ea0f8c"/><path d="M10 15l-1 3 3-3z" fill="#ea0f8c"/></svg>
      +51 917 208 386
    </span>
    <span class="contacts__sep">|</span>
    <span class="contacts__item">
      <svg class="icon" viewBox="0 0 26 26"><circle cx="13" cy="13" r="13" fill="#ea0f8c"/><rect x="7" y="8.5" width="12" height="9" rx="1" fill="none" stroke="#fff" stroke-width="1.6"/><path d="M7.5 9.5l5.5 4 5.5-4" fill="none" stroke="#fff" stroke-width="1.6"/></svg>
      tim@palduro.org
    </span>
    <span class="contacts__sep">|</span>
    <span class="contacts__item">
      <svg class="icon" viewBox="0 0 26 26"><circle cx="13" cy="13" r="13" fill="#ea0f8c"/><circle cx="13" cy="13" r="6.5" fill="none" stroke="#fff" stroke-width="1.5"/><ellipse cx="13" cy="13" rx="3" ry="6.5" fill="none" stroke="#fff" stroke-width="1.3"/><path d="M6.5 13h13" stroke="#fff" stroke-width="1.3"/></svg>
      palduro.org
    </span>
  </div>

  <svg class="bands" viewBox="0 0 733 428" aria-hidden="true">
    <polygon points="352,393 733,393 733,428 390,428" fill="#ea0f8c"/>
    <polygon points="0,386 340,386 382,428 0,428" fill="#111111"/>
  </svg>
  <div class="values values--core">Futuro<span class="bullet"></span>Liderazgo<span class="bullet"></span>Crecimiento</div>
  <div class="values values--more">Igualdad<span class="bullet"></span>Innovación<span class="bullet"></span>Sostenibilidad</div>
</section>

<section class="card card--en" lang="en">
  <div class="motif" role="img" aria-label="Faint decorative motif of the organisation emblem"></div>

  <div class="brand">
    <div class="brand__dot"></div>
    <div class="brand__text">
      <div class="brand__name">PALDURO</div>
      <div class="brand__slogan">SHAPE YOUR WORLD!</div>
    </div>
  </div>

  <div class="person">
    <div class="person__name">TIM HALLOX</div>
    <div class="person__role">MENTORING COORDINATOR</div>
  </div>

  <div class="rule"></div>

  <div class="contacts">
    <span class="contacts__item">
      <svg class="icon" viewBox="0 0 26 26"><circle cx="13" cy="13" r="13" fill="#fff"/><path d="M9 7c1 0 2 2 2 3s-1 1-1 2 3 4 4 4 1-1 2-1 3 1 3 2-1 2-3 2C12 19 7 14 7 9c0-1 1-2 2-2z" fill="#ea0f8c"/></svg>
      <svg class="icon" viewBox="0 0 26 26"><circle cx="13" cy="13" r="13" fill="#fff"/><rect x="7.5" y="8.5" width="11" height="7" rx="2" fill="#ea0f8c"/><path d="M10 15l-1 3 3-3z" fill="#ea0f8c"/></svg>
      +51 917 208 386
    </span>
    <span class="contacts__sep">|</span>
    <span class="contacts__item">
      <svg class="icon" viewBox="0 0 26 26"><circle cx="13" cy="13" r="13" fill="#fff"/><rect x="7" y="8.5" width="12" height="9" rx="1" fill="none" stroke="#ea0f8c" stroke-width="1.6"/><path d="M7.5 9.5l5.5 4 5.5-4" fill="none" stroke="#ea0f8c" stroke-width="1.6"/></svg>
      tim@palduro.org
    </span>
    <span class="contacts__sep">|</span>
    <span class="contacts__item">
      <svg class="icon" viewBox="0 0 26 26"><circle cx="13" cy="13" r="13" fill="#fff"/><circle cx="13" cy="13" r="6.5" fill="none" stroke="#ea0f8c" stroke-width="1.5"/><ellipse cx="13" cy="13" rx="3" ry="6.5" fill="none" stroke="#ea0f8c" stroke-width="1.3"/><path d="M6.5 13h13" stroke="#ea0f8c" stroke-width="1.3"/></svg>
      palduro.org
    </span>
  </div>

  <svg class="bands" viewBox="0 0 733 428" aria-hidden="true">
    <polygon points="355,393 733,393 733,428 392,428" fill="#ffffff"/>
    <polygon points="0,386 340,386 382,428 0,428" fill="#111111"/>
  </svg>
  <div class="values values--core">Future<span class="bullet"></span>Growth<span class="bullet"></span>Leadership</div>
  <div class="values values--more">Igualdad<span class="bullet"></span>Innovación<span class="bullet"></span>Sostenibilidad</div>
</section>

</body>
</html>
```